Business Card for Musician

The company is called Velkor Music Entertainment and i am the director (Miles Tenney) . I would like a logo made along with a list of services i provide :

Rock Pop and Jazz Covers music for Weddings , Birthdays , Pubs, Bars and Restaurants

I provide Solo/Duo and Bands for these functions.

Another aspect is i teach guitar and do music workshops and compose music for television.

I want to go for something different than a photo of a guitar or singer..i like the idea of soundwaves and an ear. or ripples of sound like a music note (as a drop of water) and the sound rippling out..another idea is something with lighting (music lights) with different colours lighting up the name Velkor..however im open to any ideas. Thanks

Target Market(s)

General Public, Music Agents, Venue Owners. English Speaking..adults from 25-50

Industry/Entity Type

Business

Font styles to use
Sans Serif

Colors

Designer to choose colors to be used in the design.

Requirements
Must have
• All the points about what i do...
Nice to have
• Logo could emphasize the VEL in Velkor...
Should not have
• Not too busy please...Simple but gets the message across. NOthing obvious like a photo of a musician playing.

```html
<!DOCTYPE html>
<html lang="en">
<head>
<meta charset="utf-8">
<title>Velkor Music Entertainment – Business Card</title>
<link rel="stylesheet" href="https://fonts.googleapis.com/css2?family=Lato:wght@700&family=Nunito+Sans:wght@400&display=swap">
<style>
  :root {
    --card-bg: #222222;
    --glow-teal: rgba(26, 155, 160, 0.16);
    --glow-fade: rgba(26, 155, 160, 0);
    --accent-blue: #1b96d8;
    --text-light: #ffffff;
  }
  html, body {
    margin: 0;
    padding: 0;
    overflow: hidden;
    background: var(--card-bg);
  }
  .card {
    position: relative;
    width: 1200px;
    height: 689px;
    background: var(--card-bg);
    overflow: hidden;
    font-family: "Nunito Sans", Arial, sans-serif;
    color: var(--text-light);
  }
  .backdrop {
    position: absolute;
    inset: 0;
    background: radial-gradient(circle at 115px 90px, var(--glow-teal) 0, var(--glow-fade) 480px);
  }
  .brand-mark {
    position: absolute;
    left: 62px;
    top: 37px;
    width: 106px;
    height: 106px;
    box-sizing: border-box;
    border: 5px solid var(--accent-blue);
    border-radius: 50%;
  }
  .brand-name {
    position: absolute;
    left: 186px;
    top: 60px;
    margin: 0;
    font-family: "Lato", Arial, sans-serif;
    font-weight: 700;
    font-size: 37px;
    line-height: 47px;
    letter-spacing: -1px;
    text-transform: uppercase;
    color: var(--text-light);
  }
  .contact {
    position: absolute;
    left: 784px;
    top: 64px;
    margin: 0;
    font-size: 29px;
    line-height: 37px;
  }
  .contact-name { color: var(--accent-blue); display: block; }
  .contact-role { color: var(--text-light); display: block; }
  .services {
    position: absolute;
    margin: 0;
    padding: 0;
    list-style: none;
    font-size: 29px;
    letter-spacing: 0.4px;
    line-height: 70.7px;
  }
  .services-performance {
    right: 455px;
    top: 222px;
    text-align: right;
  }
  .services-teaching {
    left: 790px;
    top: 293px;
  }
</style>
</head>
<body>
  <main class="card">
    <div class="backdrop" role="img" aria-label="Soft teal glow suggesting sound rippling out from the brand mark"></div>

    <div class="brand-mark" aria-hidden="true"></div>
    <h1 class="brand-name">Velkor Music<br>Entertainment</h1>

    <p class="contact">
      <span class="contact-name">Miles Tenney</span>
      <span class="contact-role">Director</span>
    </p>

    <ul class="services services-performance">
      <li>Solo/Duo/Band</li>
      <li>Pop/Rock/Jazz</li>
      <li>Cover Music</li>
      <li>Weddings/Birthdays</li>
      <li>Restaurants/Bars/Pubs</li>
    </ul>

    <ul class="services services-teaching">
      <li>Guitar Tutoring</li>
      <li>Music Workshop</li>
      <li>Music for Television</li>
    </ul>
  </main>
</body>
</html>
```